established boer goat stud and dorper sheep stud need an updated look

I need a design to promote the boer goat stud and dorper sheep stud, so its clear and simple

Details for business card design Tallowen Boers and Dorper Sheep Stud. I would like silhouette animal head or full body of a boer goat (not a dairy breed goat) and Dorper sheep. Contact: Renee Oakhurst +61 455018273 Debra Pellinger +61 438617204 Mooroopna North Victoria Australia Email: tallowen5184@paddockmail.net

Industry/Entity Type

Agriculture

Contact Information for Business Card

Tallowen Boers and Dorper Sheep Stud Renee Oakhurst +61 455018273 Debra Pellinger +61 438617204 tallowen5184@paddockmail.net Wendarra Victoria Australia

Colors
EE7325
F08F49
F5BC92
FAE3D3
FDF4ED

Requirements
Must have
• My Boer Goats and Dorper Sheep images see my photos

```html
<!DOCTYPE html>
<html lang="en">
<head>
<meta charset="utf-8">
<title>Tallowen Boers and Dorper Sheep Stud – Business Card</title>
<link href="https://fonts.googleapis.com/css2?family=Bebas+Neue&family=Poppins:wght@400&display=swap" rel="stylesheet">
<style>
  :root {
    --bg: #9a9fa2;
    --orange-deep: #e4702b;
    --orange-mid: #ec9257;
    --orange-light: #f0a674;
    --hill-warm: #c98d66;
    --grass: #008c3a;
    --white: #ffffff;
    --ink: #1e1a1a;
    --brand-orange: #e2631c;
    --brand-brown: #4a2c25;
    --hill-grey: #cfcaca;
    --animal-cream: #f7ead6;
    --animal-brown: #5a403a;
  }
  * { margin: 0; padding: 0; box-sizing: border-box; }
  html, body { width: 1200px; height: 928px; overflow: hidden; }
  body { background: var(--bg); position: relative; font-family: "Poppins", sans-serif; }

  .card {
    position: absolute;
    left: 258px;
    width: 688px;
    overflow: hidden;
  }
  .card--front { top: 51px; height: 397px; background: linear-gradient(to bottom, var(--orange-deep) 0%, var(--orange-mid) 45%, var(--orange-light) 75%); }
  .card--back { top: 480px; height: 393px; background: var(--white); }

  .scenery { position: absolute; left: 0; bottom: 0; width: 100%; }
  .card--front .scenery { height: 110px; background: linear-gradient(to bottom, var(--hill-warm) 0%, var(--grass) 55%); }
  .card--back .scenery { height: 160px; background: linear-gradient(to bottom, var(--hill-grey) 0%, var(--hill-grey) 35%, var(--grass) 70%); }

  .animals {
    position: absolute;
    border-radius: 30px 30px 8px 8px;
    background: linear-gradient(to right, var(--animal-cream) 0%, var(--animal-cream) 34%, var(--animal-brown) 42%, var(--animal-brown) 50%, var(--animal-cream) 58%);
    opacity: 0.85;
  }
  .card--front .animals { left: 226px; top: 105px; width: 233px; height: 92px; }
  .card--back .animals { left: 111px; top: 115px; width: 184px; height: 75px; opacity: 0.7; }

  .brand { position: absolute; font-family: "Bebas Neue", sans-serif; font-weight: 400; text-align: center; line-height: 1; }
  .brand__name { display: block; letter-spacing: 0.5px; }
  .brand__tagline { display: block; }

  .card--front .brand { left: 200px; top: 198px; width: 288px; color: var(--white); }
  .card--front .brand__name { font-size: 78px; line-height: 70px; }
  .card--front .brand__tagline { font-size: 24px; line-height: 24px; margin-top: 2px; }

  .card--back .brand { left: 98px; top: 188px; width: 210px; color: var(--brand-orange); }
  .card--back .brand__name { font-size: 60px; line-height: 56px; }
  .card--back .brand__tagline { font-size: 19px; line-height: 19px; margin-top: 2px; color: var(--brand-brown); }

  .contact { position: absolute; left: 342px; top: 133px; color: var(--ink); }
  .contact__name { font-family: "Bebas Neue", sans-serif; font-weight: 400; font-size: 34px; color: var(--brand-orange); line-height: 1; letter-spacing: 0.3px; margin-bottom: 12px; }
  .contact__row { display: flex; align-items: center; gap: 7px; font-size: 17px; line-height: 27.5px; white-space: nowrap; }
  .contact__icon { width: 17px; height: 17px; flex: none; fill: var(--ink); }
</style>
</head>
<body>

<section class="card card--front">
  <div class="scenery" role="img" aria-label="Rolling hills and green pasture grass"></div>
  <div class="animals" role="img" aria-label="Silhouettes of a Boer goat and a Dorper sheep facing each other"></div>
  <h1 class="brand">
    <span class="brand__name">Tallowen</span>
    <span class="brand__tagline">Boers and Dorper Sheep Stud</span>
  </h1>
</section>

<section class="card card--back">
  <div class="scenery" role="img" aria-label="Soft grey hills and green pasture grass"></div>
  <div class="animals" role="img" aria-label="Silhouettes of a Boer goat and a Dorper sheep facing each other"></div>
  <div class="brand">
    <span class="brand__name">Tallowen</span>
    <span class="brand__tagline">Boers and Dorper Sheep Stud</span>
  </div>

  <div class="contact">
    <h2 class="contact__name">Renee Oakhurst</h2>
    <p class="contact__row">
      <svg class="contact__icon" viewBox="0 0 24 24" aria-hidden="true"><path d="M6.6 10.8a15.1 15.1 0 0 0 6.6 6.6l2.2-2.2a1 1 0 0 1 1-.25 11.4 11.4 0 0 0 3.6.57 1 1 0 0 1 1 1V20a1 1 0 0 1-1 1A17 17 0 0 1 3 4a1 1 0 0 1 1-1h3.5a1 1 0 0 1 1 1c0 1.25.2 2.45.57 3.57a1 1 0 0 1-.25 1z"/></svg>
      +61 455018273
    </p>
    <p class="contact__row">
      <svg class="contact__icon" viewBox="0 0 24 24" aria-hidden="true"><path d="M2 5h20v2l-10 6L2 7z"/><path d="M2 9l10 6 10-6v10H2z"/></svg>
      tallowen5184@paddockmail.net
    </p>
    <p class="contact__row">
      <svg class="contact__icon" viewBox="0 0 24 24" aria-hidden="true"><path d="M12 1a8 8 0 0 0-8 8c0 6 8 14 8 14s8-8 8-14a8 8 0 0 0-8-8zm0 11a3 3 0 1 1 0-6 3 3 0 0 1 0 6z"/></svg>
      Wendarra Victoria Australia
    </p>
  </div>
</section>

</body>
</html>
```